Brovelline International is looking for web design

I have a website that I made myself and I wanted to have a more professional design. go to my website www.BrovellinePX.example and you will see what it is all about. My website was created with Weebly. we like to focus on that we have an earth friendly product. we offer a natural alternative to asphalt or concrete .

Target Market(s)

Landscape Archtects, Home Improvement , designers, parks and recreation

Industry/Entity Type

It Professional

Coding

Coded - Design and coding required

Number of Pages Required

5+ page

Requirements
Must have
• Landing page,
• Products Page contact us page

```html
<!DOCTYPE html>
<html lang="en">
<head>
<meta charset="utf-8">
<title>Advantages – Brovelline International</title>
<link href="https://fonts.googleapis.com/css2?family=Abel&family=Montserrat:wght@300;400;500&family=Roboto:wght@300;400;500&display=swap" rel="stylesheet">
<style>
  :root {
    --black: #050505;
    --white: #ffffff;
    --teal: #2f5f5a;
    --sand: #d1b283;
    --footer-sand: #cfb188;
    --ink: #2a2a2a;
    --muted: #666;
    --field-border: #d9d9d9;
    --green: #8bc34a;
    --nav-text: #555;
  }
  * { box-sizing: border-box; margin: 0; padding: 0; }
  html, body { width: 865px; height: 1200px; overflow: hidden; background: var(--white); }
  body { position: relative; font-family: "Roboto", sans-serif; color: var(--ink); }

  .topbar { position: absolute; left: 0; top: 0; width: 865px; height: 28px; background: var(--black); color: var(--white); font-size: 8px; }
  .topbar .item { position: absolute; top: 0; height: 28px; display: flex; align-items: center; gap: 6px; }
  .topbar .sep { position: absolute; top: 9px; font-size: 8px; }
  .topbar svg { stroke: var(--white); fill: none; stroke-width: 1.2; }

  .navbar { position: absolute; left: 0; top: 28px; width: 865px; height: 53px; background: var(--white); }
  .brand { position: absolute; left: 71px; top: 14px; display: flex; align-items: center; gap: 6px; font-family: "Montserrat", sans-serif; font-weight: 500; font-size: 22px; letter-spacing: 0.5px; color: var(--teal); }
  .brand .mark { width: 12px; height: 12px; background: var(--teal); }
  .nav { position: absolute; top: 0; left: 330px; height: 53px; display: flex; }
  .nav a { display: flex; align-items: center; height: 53px; padding: 0 11px; font-size: 9.5px; letter-spacing: 2.2px; color: var(--nav-text); text-decoration: none; text-transform: uppercase; font-weight: 400; }
  .nav a.active { background: var(--teal); color: var(--white); }

  .hero { position: absolute; left: 0; top: 81px; width: 865px; height: 203px; background: linear-gradient(100deg, #233a1f 0%, #3d5a2c 35%, #2c3f22 60%, #4a5a3a 100%); }
  .hero h1 { position: absolute; left: 69px; top: 144px; font-family: "Roboto", sans-serif; font-weight: 300; font-size: 27px; letter-spacing: 7px; color: var(--white); }

  .advantages { position: absolute; left: 0; top: 284px; width: 865px; height: 564px; background: var(--sand); }
  .tile { position: absolute; width: 356px; height: 151px; display: flex; align-items: center; justify-content: center; text-align: center; font-family: "Montserrat", sans-serif; font-weight: 300; font-size: 18.5px; line-height: 22px; color: var(--white); text-transform: uppercase; }
  .t1 { left: 71px; top: 46px; background: linear-gradient(135deg, #3f5a26, #2c3e1c); }
  .t2 { left: 438px; top: 46px; background: linear-gradient(135deg, #3a3a34, #4c4538); }
  .t3 { left: 71px; top: 208px; background: linear-gradient(180deg, #4a4a48, #3a3b3d); }
  .t4 { left: 438px; top: 208px; background: linear-gradient(135deg, #34392c, #5b6052); }
  .t5 { left: 71px; top: 370px; background: linear-gradient(135deg, #4a5058, #5d6670); }
  .t6 { left: 438px; top: 370px; background: linear-gradient(135deg, #36502a, #2a4020); }

  .contact-intro { position: absolute; left: 71px; top: 888px; width: 270px; font-family: "Abel", sans-serif; }
  .contact-intro h2 { font-weight: 400; font-size: 24px; color: #666; }
  .contact-intro p { margin-top: 14px; font-size: 14px; line-height: 18.5px; color: var(--ink); }
  .info { position: absolute; left: 71px; display: flex; gap: 12px; }
  .info .icon { width: 25px; height: 25px; border-radius: 50%; background: var(--teal); display: flex; align-items: center; justify-content: center; margin-top: 1px; }
  .info .icon svg { stroke: var(--white); fill: none; stroke-width: 1.3; }
  .info .label { font-family: "Abel", sans-serif; font-size: 12px; color: var(--ink); }
  .info .value { font-family: "Montserrat", sans-serif; font-size: 11px; color: var(--ink); margin-top: 1px; }

  .contact-form h2 { position: absolute; left: 371px; top: 883px; font-family: "Abel", sans-serif; font-weight: 400; font-size: 26px; letter-spacing: 1px; color: var(--ink); }
  .field { position: absolute; border: 1px solid var(--field-border); font-family: "Montserrat", sans-serif; font-size: 8.5px; color: #999; padding: 10px 13px; }
  .submit { position: absolute; left: 726px; top: 1107px; width: 67px; height: 23px; background: var(--green); color: var(--white); font-family: "Montserrat", sans-serif; font-size: 9px; font-weight: 500; display: flex; align-items: center; justify-content: center; }

  .footer { position: absolute; left: 0; top: 1158px; width: 865px; height: 42px; background: var(--footer-sand); }
  .footer p { position: absolute; left: 71px; top: 16px; font-family: "Abel", sans-serif; font-size: 9.5px; color: var(--white); }
</style>
</head>
<body>

<header class="topbar">
  <div class="item" style="left:71px;">
    <svg width="8" height="13" viewBox="0 0 8 13"><rect x="0.6" y="0.6" width="6.8" height="11.8" rx="1"/></svg>
    <span style="font-weight:500;">555-014-7334</span>
  </div>
  <span class="sep" style="left:148px;">|</span>
  <div class="item" style="left:162px;">
    <svg width="14" height="10" viewBox="0 0 14 10"><rect x="0.6" y="0.6" width="12.8" height="8.8"/><path d="M0.6 0.6 L7 5.5 L13.4 0.6"/></svg>
    <span>info@brovelline.example</span>
  </div>
  <span class="sep" style="left:668px;">|</span>
  <div class="item" style="left:683px;">
    <svg width="12" height="12" viewBox="0 0 12 12"><path d="M1 11 L2 8 L9 1 L11 3 L4 10 Z"/></svg>
    <span>Register</span>
  </div>
  <span class="sep" style="left:741px;">|</span>
  <div class="item" style="left:756px;">
    <svg width="11" height="10" viewBox="0 0 11 10"><path d="M5 0.6 H10.4 V9.4 H5 M0.5 5 H7 M5 3 L7 5 L5 7"/></svg>
    <span>Login</span>
  </div>
</header>

<nav class="navbar">
  <div class="brand"><span class="mark"></span>VERDALITH</div>
  <div class="nav">
    <a>General Info</a>
    <a>FAQ</a>
    <a class="active">Advantages</a>
    <a>Applications</a>
    <a>Video's</a>
    <a>Resellers</a>
  </div>
</nav>

<section class="hero" role="img" aria-label="Photo of a dense green forest with mossy tree trunks">
  <h1>ADVANTAGES</h1>
</section>

<section class="advantages">
  <div class="tile t1" role="img" aria-label="Sunlit forest floor">Natural,<br>earth-friendly product</div>
  <div class="tile t2" role="img" aria-label="Cleared forest with timber debris">Produced using sustainable<br>forestry practices</div>
  <div class="tile t3" role="img" aria-label="Paved driveway in front of a garage">Beautiful, durable<br>alternative to asphalt</div>
  <div class="tile t4" role="img" aria-label="Garden patio with paving and furniture">Stronger than other<br>paving alternatives</div>
  <div class="tile t5" role="img" aria-label="Rows of paving panels under installation">Cooler in summer</div>
  <div class="tile t6" role="img" aria-label="Paved trail through woodland">Meets ADA guidelines</div>
</section>

<section class="contact">
  <div class="contact-intro">
    <h2>We would Love To Hear</h2>
    <p>Give us a call or send us a message using the form below.</p>
  </div>
  <div class="info" style="top:979px;">
    <div class="icon"><svg width="11" height="14" viewBox="0 0 11 14"><path d="M5.5 13 C2 8.5 1 6.5 1 5 A4.5 4.5 0 0 1 10 5 C10 6.5 9 8.5 5.5 13 Z"/><circle cx="5.5" cy="5" r="1.6"/></svg></div>
    <div><div class="label">ADDRESS</div><div class="value">Brovelline International 123 road</div></div>
  </div>
  <div class="info" style="top:1030px;">
    <div class="icon"><svg width="12" height="12" viewBox="0 0 12 12"><path d="M2 1.5 L4 1.5 L5 4 L3.8 5 C4.5 6.5 5.5 7.5 7 8.2 L8 7 L10.5 8 L10.5 10 C6 10.5 1.5 6 2 1.5 Z"/></svg></div>
    <div><div class="label">PHONES</div><div class="value">555-014-7334</div></div>
  </div>
  <div class="info" style="top:1080px;">
    <div class="icon"><svg width="13" height="10" viewBox="0 0 13 10"><rect x="0.6" y="0.6" width="11.8" height="8.8"/><path d="M0.6 0.6 L6.5 5.5 L12.4 0.6"/></svg></div>
    <div><div class="label">EMAIL</div><div class="value">info@brovelline.example</div></div>
  </div>

  <div class="contact-form">
    <h2>CONTACT US &amp; ASK THE EXPERTS</h2>
    <div class="field" style="left:372px;top:934px;width:200px;height:30px;">Name</div>
    <div class="field" style="left:592px;top:934px;width:201px;height:30px;">Email</div>
    <div class="field" style="left:371px;top:976px;width:422px;height:32px;">Subject</div>
    <div class="field" style="left:371px;top:1020px;width:422px;height:76px;padding-top:8px;">Message...</div>
    <div class="submit">SUBMIT</div>
  </div>
</section>

<footer class="footer">
  <p>© Copyright 2016 Brovelline International, All rights reserved</p>
</footer>

</body>
</html>
```